High-End audio shop owner needs a business card

I need a personal Business Card for my Audio shop which exists since 1962. We offer high Quality brands, professional Attention and run our own repair-service-department. I look for a design which will be printed on high Quality paper and shall convey trust to the Client that we are very serious. Language is german.

```html
<!DOCTYPE html>
<html lang="de">
<head>
<meta charset="utf-8">
<title>Hi-Fi Adlerhaus – Visitenkarte</title>
<link rel="stylesheet" href="https://fonts.googleapis.com/css2?family=Montserrat:wght@800&family=Roboto:wght@400&display=swap">
<style>
  :root {
    --stage: #2a2a2a;
    --card-grey: #868b88;
    --card-white: #ffffff;
    --brand-orange: #f07622;
    --accent-grey: #7d827f;
    --text-grey: #9a9a9a;
    --text-dark: #3a3a3a;
  }
  * { margin: 0; padding: 0; box-sizing: border-box; }
  html, body { width: 1200px; height: 900px; overflow: hidden; background: var(--stage); }
  .stage {
    width: 1200px; height: 900px;
    display: flex; flex-direction: column; align-items: center; justify-content: center; gap: 36px;
  }
  .card {
    position: relative; width: 700px; height: 400px; overflow: hidden;
    box-shadow: 0 10px 30px rgba(0,0,0,.45);
  }
  .card--front { background: var(--card-grey); display: flex; align-items: center; justify-content: center; }
  .card--back { background: var(--card-white); }
  .brand-name {
    font-family: "Montserrat", sans-serif; font-weight: 800;
    color: var(--brand-orange); letter-spacing: 1px; white-space: nowrap;
    display: flex; align-items: center; gap: 12px;
  }
  .brand-name__dot { width: 14px; height: 14px; border-radius: 50%; background: var(--brand-orange); }
  .card--front .brand-name { font-size: 46px; }
  .card--back .brand-name { position: absolute; right: 40px; top: 110px; font-size: 30px; }
  .divider { position: absolute; left: 40px; right: 30px; top: 200px; height: 2px; background: var(--brand-orange); }
  .person { position: absolute; left: 40px; top: 128px; }
  .person__name { font-family: "Montserrat", sans-serif; font-weight: 800; font-size: 28px; color: var(--brand-orange); }
  .person__role { font-family: "Roboto", sans-serif; font-size: 15px; color: var(--text-grey); margin-top: 4px; }
  .contact { position: absolute; left: 40px; top: 218px; list-style: none;
    font-family: "Roboto", sans-serif; font-size: 16px; color: var(--text-dark); }
  .contact li { display: flex; align-items: center; gap: 10px; height: 24px; }
  .contact svg { width: 13px; height: 13px; fill: var(--brand-orange); flex: none; }
  .swoosh { position: absolute; inset: 0; }
</style>
</head>
<body>
<main class="stage">
  <section class="card card--front">
    <div class="brand-name"><span class="brand-name__dot"></span>Hi-Fi Adlerhaus</div>
  </section>

  <section class="card card--back">
    <svg class="swoosh" viewBox="0 0 700 400" aria-hidden="true">
      <path fill="var(--accent-grey)" d="M165,392 C275,282 430,312 560,272 C620,254 662,236 692,218 C664,246 622,268 566,286 C432,328 285,300 165,392Z"/>
      <path fill="var(--brand-orange)" d="M150,400 C260,300 420,332 565,294 C625,278 670,250 700,226 L700,400Z"/>
    </svg>

    <div class="brand-name"><span class="brand-name__dot"></span>Hi-Fi Adlerhaus</div>

    <div class="person">
      <h1 class="person__name">Lukas Berger</h1>
      <p class="person__role">General Manager</p>
    </div>
    <div class="divider"></div>

    <ul class="contact">
      <li><svg viewBox="0 0 16 16"><path d="M3 1l3 3-2 2c1 2 4 5 6 6l2-2 3 3-2 2C7 15 1 9 1 3z"/></svg>02 5550 1870</li>
      <li><svg viewBox="0 0 16 16"><path d="M4 0h8a1 1 0 0 1 1 1v14a1 1 0 0 1-1 1H4a1 1 0 0 1-1-1V1a1 1 0 0 1 1-1zm1 2v10h6V2z"/></svg>0411 555 019</li>
      <li><svg viewBox="0 0 16 16"><path d="M0 3h16v10H0zm2 1.5V5l6 4 6-4v-.5z"/></svg>kontakt@adlerhaus-audio.de</li>
      <li><svg viewBox="0 0 16 16"><circle cx="8" cy="8" r="7"/></svg>www.adlerhaus-audio.de</li>
    </ul>
  </section>
</main>
</body>
</html>
```